Designing promotion page - poster for Folk High School

I would like a attractive and well-designed page /poster used in a catalogue for the Tavelund Learning Colleges.
The dimensions on the graphical element:
Width: 180 mm
Hight:186 mm
Resolution: min. 450 dpi
This graphical element will be combined with other information about the school, that is static and we cannot change. Please see attachment (“Folk High School – placement of graphic”). The almost square area in the middle of the page iss the one that the designed grapichal element will fill.
A part of completing this, is to hand over the workfile to us in the end when we choose the design (Adobe Photoshop PSD or an InDesign INDD file must be used)
There are also attached some pictures that you are free to use in creating the design as you like. You will choose how many pictures you want to use. Please cut, scale, adjust and sharpen them as you like. Only one requirement: Please use one of the Sri Lanka pictures.
Be creative.
The following text-elements must be used in the page (They are also prioritized – number one means: most important that the reader reads…)
1. Møtet som forandrer --- headline. Yep; needs a font supporting ÆØÅ...
2. Multisport --- different courses we provide at our school.
- Data Media – Japan
- Barn i Fokus
- Helse og Velvære
- Globalt Fokus – Afrika
- Fotball
- Bil og Motor
- Internasjonal
- Worship – Australia
- KISS-friluft
- Høy Puls
Alle linjer reiser på egne turer i inn –og utland! ---- This should be included as the different courses, but in the bottum of the «box».
3. Spennende fellestur for alle til Sri Lanka ---- Use together with the picture from Sri Lanke (Not too large picture!)
4. Hva skal du bli? ---- small headline.
Vi er gode på veiledning, og hjelper deg med å finne ut hva du skal bli.
5. Flott skole:
- Basseng
- Styrkerom
- Gymsal
- Internatstuer
- Filmsal
- Skolekjøkken
- Verksted
- Fotostudio
- Fitnessrom
_________
The students attending our school is between 18-20 years. Of course, the design and expression must meet their expectations.
Looking forward to see the first drafts!
To understand what this should look like: Check the following link:
https://leafrack.net/tavelundskolen/docs/tlc_guide__18__web
The poster / graphic we want to create, is similar to the one you find in this brochure from page 20.

```html
<!DOCTYPE html>
<html lang="no">
<head>
<meta charset="utf-8">
<title>Møtet som forandrer – Tavelund Learning Colleges</title>
<link rel="stylesheet" href="https://fonts.googleapis.com/css2?family=Raleway:wght@300;400;500;600;700&display=swap">
<style>
  :root {
    --backdrop: #a6a7aa;
    --headline: #f0a224;
    --white: #ffffff;
    --blue-head: #5a88c3;
    --blue-text: #6892c8;
    --bar: #000000;
  }
  * { box-sizing: border-box; margin: 0; padding: 0; }
  html, body { width: 1200px; height: 1190px; overflow: hidden; background: var(--backdrop); }
  body { font-family: "Raleway", sans-serif; position: relative; }

  .poster {
    position: absolute; left: 25px; top: 1px;
    width: 1150px; height: 1188px; overflow: hidden;
  }

  .hero {
    position: absolute; left: 0; top: 0; width: 1150px; height: 758px;
  }
  .hero-photo {
    position: absolute; inset: 0;
    background:
      radial-gradient(ellipse 300px 80px at 760px 400px, rgba(255,190,60,.9), rgba(240,130,30,.45) 45%, rgba(0,0,0,0) 80%),
      linear-gradient(90deg, rgba(0,0,0,0) 60%, rgba(45,30,32,.45) 80%, rgba(45,30,32,.45) 100%),
      linear-gradient(180deg, #1c1c1e 0%, #3a3a3e 18%, #6f6d6e 35%, #a08066 48%, #c98a4a 54%, #5d4a2e 62%, #3a3224 75%, #2b281f 100%);
  }

  .headline {
    position: absolute; left: 52px; top: 36px;
    color: var(--headline); font-weight: 400;
    font-size: 134px; line-height: 160px; letter-spacing: -1px;
    text-transform: uppercase; white-space: nowrap;
  }

  .courses { position: absolute; left: 0; top: 0; color: var(--white); }
  .courses-title {
    position: absolute; left: 395px; top: 416px; transform: translateX(-50%);
    font-size: 29px; font-weight: 500; letter-spacing: .5px; white-space: nowrap;
  }
  .course-list {
    position: absolute; top: 462px; list-style: none;
    font-size: 31.5px; font-weight: 400; line-height: 45px; white-space: nowrap;
  }
  .course-list li::before { content: "·"; margin-right: 10px; font-weight: 700; }
  .course-list.col-a { left: 49px; }
  .course-list.col-b { left: 421px; }
  .courses-note {
    position: absolute; left: 57px; top: 698px;
    font-size: 32px; white-space: nowrap;
  }

  .guidance { position: absolute; left: 0; top: 758px; width: 645px; height: 382px; overflow: hidden; }
  .guidance-photo {
    position: absolute; inset: 0;
    background: linear-gradient(180deg, #c9dcef 0%, #eef3f8 40%, #dfe8f1 70%, #f5f7f9 100%);
  }
  .guidance-title {
    position: absolute; left: 371px; top: 0; transform: translateX(-50%);
    color: var(--blue-head); font-size: 54px; font-weight: 700; white-space: nowrap;
  }
  .guidance-text {
    position: absolute; left: 17px; top: 312px;
    color: var(--blue-text); font-size: 27.5px; font-weight: 600; line-height: 32px; white-space: nowrap;
  }

  .trip { position: absolute; left: 645px; top: 758px; width: 505px; height: 382px; overflow: hidden; }
  .trip-photo {
    position: absolute; inset: 0;
    background: linear-gradient(180deg, #e7edf2 0%, #cdd7dc 30%, #7c8a5f 55%, #4f5a3d 68%, #b9b3a2 82%, #6f7f8c 100%);
  }
  .trip-caption {
    position: absolute; left: 19px; top: 344px;
    color: var(--white); font-size: 25.5px; font-weight: 600; white-space: nowrap;
  }

  .facilities {
    position: absolute; left: 0; top: 1140px; width: 1150px; height: 48px;
    background: var(--bar); color: var(--white);
    display: flex; justify-content: space-between; align-items: center;
    padding: 0 2px 0 33px; list-style: none;
    font-size: 23px; font-weight: 500; white-space: nowrap;
  }
</style>
</head>
<body>
  <main class="poster">
    <section class="hero">
      <div class="hero-photo" role="img" aria-label="Photo: four young women seen from behind watching a sunset over the savanna"></div>
      <h1 class="headline">Møtet som<br>forandrer</h1>
      <div class="courses">
        <h2 class="courses-title">MULTISPORT</h2>
        <ul class="course-list col-a">
          <li>Data Media – Japan</li>
          <li>Barn i Fokus</li>
          <li>Helse og Velvære</li>
          <li>Globalt Fokus – Afrika</li>
          <li>Fotball</li>
        </ul>
        <ul class="course-list col-b">
          <li>Bil og Motor</li>
          <li>Internasjonal</li>
          <li>Worship – Australia</li>
          <li>KISS-friluft</li>
          <li>Høy Puls</li>
        </ul>
        <p class="courses-note">Alle linjer reiser på egne turer i inn –og utland!</p>
      </div>
    </section>

    <section class="guidance">
      <div class="guidance-photo" role="img" aria-label="Photo: four young men jumping in the air against a cloudy blue sky"></div>
      <h2 class="guidance-title">Hva skal du bli?</h2>
      <p class="guidance-text">Vi er gode på veiledning,<br>og hjelper deg med å finne ut hva du skal bli.</p>
    </section>

    <section class="trip">
      <div class="trip-photo" role="img" aria-label="Photo: stilt fishermen on poles by the shore under palm trees in Sri Lanka"></div>
      <p class="trip-caption">Spennende fellestur for alle til Sri Lanka</p>
    </section>

    <ul class="facilities">
      <li>Basseng</li>
      <li>Styrkerom</li>
      <li>Gymsal</li>
      <li>Internatstuer</li>
      <li>Filmsal</li>
      <li>Skolekjøkken</li>
      <li>Verksted</li>
      <li>Fotostudio</li>
      <li>Fitnessrom</li>
    </ul>
  </main>
</body>
</html>
```